New business card design needed for Trucking/Staffing company!

I am looking for a business card design. The business name is Harbor Lane Freightworks, LLC. This company is a staffing company for commercial drivers/truck drivers. Most of our customers are trucking/supply companies. Our colors are blue/black/white/grey. The info I have on my current business cards is
-Spot for a name
-2 lines for an address
-3 lines for Office, cell, and fax
-email
-website(currently on backside of card with logo but can go anywhere)
Updates

Project Deadline Extended
Reason: Open to more designs

Target Market(s)

Trucking companies, building supply companies

Industry/Entity Type

Business

Contact Information for Business Card

Edgy but professional

Font styles to use
Other font styles liked:
• Open to suggestions

Colors
0555a3
000000
ffffff
9d9d9d

Requirements
Must have
• Must have the logo incorporated

```html
<!DOCTYPE html>
<html lang="en">
<head>
<meta charset="utf-8">
<title>Harbor Lane Freightworks, LLC — Business Card</title>
<link rel="stylesheet" href="https://fonts.googleapis.com/css2?family=EB+Garamond:wght@400;600&display=swap">
<style>
  :root {
    --brand-blue: #0555a3;
    --ink-black: #000000;
    --paper-white: #ffffff;
    --steel-grey: #9d9d9d;
    --text-dark: #3a3a3a;
    --backdrop: #e4e4e4;
  }
  * { box-sizing: border-box; margin: 0; padding: 0; }
  html, body {
    width: 1200px; height: 800px; overflow: hidden;
    background: radial-gradient(ellipse at center, #f4f4f4 0%, var(--backdrop) 60%, #c9c9c9 100%);
    font-family: "EB Garamond", Georgia, serif;
  }
  .canvas {
    position: relative; width: 1200px; height: 800px;
    display: flex; align-items: center; justify-content: center; gap: 60px;
  }
  .card {
    position: relative; width: 525px; height: 300px; border-radius: 24px;
    box-shadow: 0 14px 30px rgba(0,0,0,0.28);
    overflow: hidden;
  }
  .card--back { background: var(--ink-black); }
  .card--front { background: var(--paper-white); }

  .company-name {
    font-family: "EB Garamond", Georgia, serif;
    font-weight: 600; color: var(--brand-blue);
    letter-spacing: 0.5px; line-height: 1.05;
    display: flex; align-items: center; gap: 12px;
  }
  .company-name__dot {
    width: 14px; height: 14px; border-radius: 50%;
    background: var(--brand-blue); flex: none;
  }

  .card--back .company-name {
    position: absolute; left: 70px; top: 92px; font-size: 34px;
  }
  .card--back .website {
    position: absolute; left: 120px; top: 205px;
    color: var(--paper-white); font-size: 17px;
  }

  .card--front .company-name {
    position: absolute; left: 200px; top: 36px; font-size: 26px; width: 300px;
  }
  .holder {
    position: absolute; left: 36px; top: 150px; width: 150px; text-align: center;
  }
  .holder__name {
    font-variant: small-caps; font-weight: 600; color: var(--brand-blue);
    font-size: 25px; letter-spacing: 0.5px;
  }
  .holder__position {
    display: flex; align-items: center; gap: 6px; justify-content: center;
    font-size: 12px; letter-spacing: 1.5px; color: var(--text-dark); margin-top: 2px;
  }
  .holder__position::before, .holder__position::after {
    content: ""; flex: 1; height: 1px; background: var(--text-dark);
  }
  .divider {
    position: absolute; left: 212px; top: 132px; width: 2px; height: 118px;
    background: var(--text-dark);
  }
  .contact-list {
    position: absolute; left: 238px; top: 128px; list-style: none;
    font-size: 15px; color: var(--text-dark); line-height: 1.15;
  }
  .contact-list li { display: flex; align-items: flex-start; gap: 9px; margin-bottom: 3px; }
  .contact-icon { width: 15px; height: 15px; flex: none; margin-top: 2px; }
  .contact-icon circle { fill: var(--brand-blue); }
  .contact-icon .glyph { fill: var(--paper-white); }
  .contact-list .address { padding-left: 24px; margin-top: -3px; }
</style>
</head>
<body>
<main class="canvas">
  <section class="card card--back" aria-label="Card back">
    <div class="company-name"><span class="company-name__dot"></span>Harbor Lane<br>Freightworks</div>
    <p class="website">www.harborlanefreightworks.com</p>
  </section>

  <section class="card card--front" aria-label="Card front">
    <div class="company-name"><span class="company-name__dot"></span>Harbor Lane Freightworks</div>

    <div class="holder">
      <p class="holder__name">Name Here</p>
      <p class="holder__position">POSITION</p>
    </div>

    <div class="divider"></div>

    <ul class="contact-list">
      <li>
        <svg class="contact-icon" viewBox="0 0 16 16" aria-label="Office phone"><circle cx="8" cy="8" r="8"/><path class="glyph" d="M5 4.2l1.6-.4.9 2-1 .8a5 5 0 0 0 2.9 2.9l.8-1 2 .9-.4 1.6C9 11.3 4.7 7 5 4.2z"/></svg>
        <span>123 456 789</span>
      </li>
      <li>
        <svg class="contact-icon" viewBox="0 0 16 16" aria-label="Cell phone"><circle cx="8" cy="8" r="8"/><rect class="glyph" x="5.5" y="3.5" width="5" height="9" rx="1"/><rect x="6.3" y="4.5" width="3.4" height="6" fill="#0555a3"/></svg>
        <span>123 456 789</span>
      </li>
      <li>
        <svg class="contact-icon" viewBox="0 0 16 16" aria-label="Fax"><circle cx="8" cy="8" r="8"/><rect class="glyph" x="4" y="6.5" width="8" height="4.5" rx="0.8"/><rect class="glyph" x="5.5" y="4" width="5" height="2"/></svg>
        <span>123 456 789</span>
      </li>
      <li>
        <svg class="contact-icon" viewBox="0 0 16 16" aria-label="Email"><circle cx="8" cy="8" r="8"/><rect class="glyph" x="4" y="5" width="8" height="6" rx="0.8"/><path d="M4.3 5.4L8 8.3l3.7-2.9" stroke="#0555a3" stroke-width="0.9" fill="none"/></svg>
        <span>info@harborlanefreightworks.com</span>
      </li>
      <li>
        <svg class="contact-icon" viewBox="0 0 16 16" aria-label="Address"><circle cx="8" cy="8" r="8"/><path class="glyph" d="M8 3.5a3 3 0 0 1 3 3c0 2.2-3 6-3 6s-3-3.8-3-6a3 3 0 0 1 3-3z"/><circle cx="8" cy="6.5" r="1.1"/></svg>
        <span>Address Line 1</span>
      </li>
      <li class="address"><span>Address Line 2</span></li>
    </ul>
  </section>
</main>
</body>
</html>
```